RedField - Rebranding, Namecard, Stationary and One Page Web

Refresh logo, make it modern and design matching name card, stationary and one page web

RedField Information Technology (Int'l) Company Limited
紅原訊息科技(國際)有限公司

Company is System Integrator, and will be providing products and services to government and enterprise organizations. Our Chief Security Officer came from top U.S. vendor, and had been working on top enterprise and government projects globally, so we want the refreshed image of the new company to have a East Cost U.S. style, with hint of technology from Silicon Valley. The company will also be representing top brands from the U.S. on information security.

Branding refresh is needed because company is being acquired and is expanding

Target Market(s)

Cyber Security

Industry/Entity Type

Information Technology

Contact Information for Business Card

Need Chinese and English

Number of Pages Required

1 page

Font styles to use
Sans Serif

Colors
0292cd
00a990

Requirements
Must have
• Modern, clean, cyber look. Must keep same colors and general look and feel of original logo. Only modernization, do not change its personality

```html
<!DOCTYPE html>
<html lang="en">
<head>
<meta charset="utf-8">
<title>RedField Name Card</title>
<link rel="stylesheet" href="https://fonts.googleapis.com/css2?family=Exo+2:wght@400;600;700;800&family=Noto+Sans+TC:wght@500&display=swap">
<style>
  :root {
    --brand-blue: #0292cd;
    --brand-green: #00a990;
    --ink: #4a4a4a;
    --rule: #8a8a8a;
    --card: #ffffff;
    --map-tint: #eef0f2;
    --backdrop: #1c1c1c;
  }
  * { margin: 0; padding: 0; box-sizing: border-box; }
  html, body {
    width: 1200px; height: 1000px; overflow: hidden;
    background: var(--backdrop);
    font-family: "Exo 2", sans-serif;
  }
  .stage { position: relative; width: 1200px; height: 1000px; }
  .card {
    position: absolute;
    width: 640px; height: 366px;
    background: var(--card);
    border-radius: 28px;
    overflow: hidden;
  }
  /* Front */
  .card-front { left: 110px; top: 110px; }
  .world-map {
    position: absolute; left: 30px; top: 20px; right: 30px; bottom: 20px;
    background: radial-gradient(ellipse at center, var(--map-tint) 0%, #f6f7f8 60%, var(--card) 100%);
    border-radius: 20px;
  }
  .front-brand {
    position: absolute; left: 0; right: 0; top: 118px;
    text-align: center;
  }
  .wordmark {
    display: inline-flex; align-items: center; gap: 12px;
    font-weight: 800; color: var(--brand-blue);
    letter-spacing: 1px; text-transform: uppercase;
  }
  .wordmark .dot {
    display: inline-block; border-radius: 50%; background: var(--brand-green);
  }
  .front-brand .wordmark { font-size: 44px; }
  .front-brand .wordmark .dot { width: 22px; height: 22px; }
  .company-en {
    margin-top: 26px;
    font-size: 15px; font-weight: 600; color: var(--brand-blue);
  }
  .company-zh {
    margin-top: 4px;
    font-family: "Noto Sans TC", sans-serif;
    font-size: 14px; color: var(--brand-green);
  }
  /* Back */
  .card-back { left: 450px; top: 524px; }
  .back-brand { position: absolute; right: 40px; top: 44px; }
  .back-brand .wordmark { font-size: 34px; }
  .back-brand .wordmark .dot { width: 18px; height: 18px; }
  .divider-long {
    position: absolute; left: 300px; right: 36px; top: 146px;
    height: 1px; background: var(--rule);
  }
  .address {
    position: absolute; right: 36px; top: 160px; width: 300px;
    text-align: right; font-size: 13px; line-height: 1.45; color: var(--ink);
  }
  .person { position: absolute; left: 40px; top: 210px; }
  .person-name {
    font-size: 24px; font-weight: 700; color: var(--brand-blue);
    letter-spacing: 0.5px; text-transform: uppercase;
  }
  .person-title { font-size: 17px; color: var(--ink); margin-top: 2px; }
  .divider-short { width: 240px; height: 1px; background: var(--rule); margin-top: 8px; }
  .contacts { list-style: none; margin-top: 12px; }
  .contacts li {
    display: flex; align-items: center; gap: 12px;
    font-size: 14.5px; color: var(--ink); line-height: 1.55;
  }
  .contacts svg { width: 12px; height: 12px; fill: var(--brand-blue); flex: none; }
  .contacts .accent { color: var(--brand-blue); }
</style>
</head>
<body>
<main class="stage">

  <section class="card card-front" aria-label="Name card front">
    <div class="world-map" role="img" aria-label="Faint world map background"></div>
    <div class="front-brand">
      <div class="wordmark"><span class="dot"></span>RedField</div>
      <p class="company-en">RedField Information Technology (Int'l) Company Limited</p>
      <p class="company-zh">紅原訊息科技(國際)有限公司</p>
    </div>
  </section>

  <section class="card card-back" aria-label="Name card back">
    <div class="back-brand">
      <div class="wordmark"><span class="dot"></span>RedField</div>
    </div>
    <div class="divider-long"></div>
    <address class="address" style="font-style:normal">
      Room C, Unit 402, 4/F, Lok Tin Ind. Bldg,<br>
      No. 12 Sheung Yuet Road, Kowloon Bay,<br>
      Kowloon, HKSAR
    </address>
    <div class="person">
      <h1 class="person-name">Daniel Wong</h1>
      <p class="person-title">CEO</p>
      <div class="divider-short"></div>
      <ul class="contacts">
        <li>
          <svg viewBox="0 0 24 24" aria-hidden="true"><path d="M6.6 10.8a15.2 15.2 0 0 0 6.6 6.6l2.2-2.2a1 1 0 0 1 1-.25 11.4 11.4 0 0 0 3.6.57 1 1 0 0 1 1 1V20a1 1 0 0 1-1 1A17 17 0 0 1 3 4a1 1 0 0 1 1-1h3.5a1 1 0 0 1 1 1c0 1.25.2 2.45.57 3.57a1 1 0 0 1-.25 1z"/></svg>
          (852) 6100 2480
        </li>
        <li>
          <svg viewBox="0 0 24 24" aria-hidden="true"><path d="M2 5h20v14H2z M2 5l10 8 10-8" fill="none" stroke="#0292cd" stroke-width="2.4"/></svg>
          danielwong@hkredfield.com.hk
        </li>
        <li>
          <svg viewBox="0 0 24 24" aria-hidden="true"><circle cx="12" cy="12" r="10"/><path d="M2 12h20M12 2c3 3 3 17 0 20M12 2c-3 3-3 17 0 20" fill="none" stroke="#fff" stroke-width="1.5"/></svg>
          <span>www.<span class="accent">hkredfield</span>.com.hk</span>
        </li>
      </ul>
    </div>
  </section>

</main>
</body>
</html>
```